BrightLoop Vents Services need a Business Card!

Need a business card designed for a new start company called BrightLoop! I have attached a Zip file (Please let me know if you cannot open this file) with all logos and also a sheets that includes fonts and colors. Last, you will see the design of our vans which will help design the cards too!
The card is needing to be double sided. A place for email, name, headshot, cell #, Office #, Job Title (Head shot optional)

Target Market(s)

People who need their HVAC filters changed. Residential and Commercial

Industry/Entity Type

Hvac Filter Changing Service

Contact Information for Business Card

Website: BrightLoopVents.us Office phone: 517.268.3390 The card is needing to be double sided. A place for email, name, headshot, cell #, Office #, Job Title (Head shot optional)

Requirements
Must have
• Color code and fonts form attached sheets and files

```html
<!DOCTYPE html>
<html lang="en">
<head>
<meta charset="utf-8">
<title>BrightLoop Vents Services – Business Card</title>
<link rel="stylesheet" href="https://fonts.googleapis.com/css2?family=Montserrat:wght@400;500;700&display=swap">
<style>
  :root {
    --backdrop: #3b3b3d;
    --navy: #084a94;
    --sky: #0fa7e6;
    --paper: #ffffff;
    --ink: #3a3a3a;
  }
  * { margin: 0; padding: 0; box-sizing: border-box; }
  html, body {
    width: 1200px; height: 1200px; overflow: hidden;
    background: var(--backdrop);
    font-family: "Montserrat", sans-serif;
  }
  .sheet {
    width: 1200px; height: 1200px;
    display: flex; flex-direction: column; align-items: center; justify-content: center;
    gap: 56px;
  }
  .card {
    position: relative;
    width: 900px; height: 514px;
    border-radius: 36px;
    overflow: hidden;
    box-shadow: 0 16px 40px rgba(0,0,0,0.45);
  }
  .card--front { background: var(--paper); }
  .card--back { background: var(--navy); display: flex; align-items: center; justify-content: center; }
  .wave { position: absolute; inset: 0; width: 100%; height: 100%; }
  .brand {
    display: flex; align-items: center; gap: 16px;
    font-weight: 700; letter-spacing: -0.5px; white-space: nowrap;
  }
  .brand__dot { border-radius: 50%; flex: none; }
  .card--front .brand {
    position: absolute; left: 530px; top: 130px;
    color: var(--navy); font-size: 46px;
  }
  .card--front .brand__dot { width: 30px; height: 30px; background: var(--navy); }
  .card--back .brand { color: var(--paper); font-size: 92px; }
  .card--back .brand__dot { width: 60px; height: 60px; background: var(--paper); }
  .person { position: absolute; left: 80px; top: 125px; }
  .person__name { color: var(--sky); font-weight: 700; font-size: 38px; line-height: 1; letter-spacing: 0.5px; }
  .person__role { color: var(--ink); font-weight: 400; font-size: 22px; margin-top: 6px; letter-spacing: 0.5px; }
  .contacts { list-style: none; margin-top: 18px; }
  .contacts__item {
    display: flex; align-items: center; gap: 14px;
    color: var(--ink); font-size: 22px; line-height: 1.5;
  }
  .contacts__icon { width: 22px; height: 22px; flex: none; fill: var(--sky); }
</style>
</head>
<body>
<main class="sheet">
  <section class="card card--front" aria-label="Business card front">
    <svg class="wave" viewBox="0 0 900 514" preserveAspectRatio="none" aria-hidden="true">
      <path fill="var(--sky)" d="M0,514 L0,470 C220,370 460,380 650,345 C800,318 880,290 900,260 L900,514 Z"/>
      <path fill="var(--paper)" d="M0,514 L0,486 C220,386 460,394 650,359 C800,332 880,306 900,276 L900,514 Z"/>
      <path fill="var(--navy)" d="M0,514 L0,498 C220,398 460,406 650,371 C800,344 880,318 900,288 L900,514 Z"/>
    </svg>

    <div class="brand"><span class="brand__dot"></span>BrightLoop</div>

    <div class="person">
      <p class="person__name">FULL NAME</p>
      <p class="person__role">POSITION</p>
      <ul class="contacts">
        <li class="contacts__item">
          <svg class="contacts__icon" viewBox="0 0 24 24" aria-hidden="true"><path d="M6.6 10.8a15.1 15.1 0 0 0 6.6 6.6l2.2-2.2a1 1 0 0 1 1-.25 11.4 11.4 0 0 0 3.6.57 1 1 0 0 1 1 1V20a1 1 0 0 1-1 1A17 17 0 0 1 3 4a1 1 0 0 1 1-1h3.5a1 1 0 0 1 1 1c0 1.25.2 2.45.57 3.6a1 1 0 0 1-.25 1z"/></svg>
          517.268.3390
        </li>
        <li class="contacts__item">
          <svg class="contacts__icon" viewBox="0 0 24 24" aria-hidden="true"><path d="M2 5h20v14H2z M3.5 6.5 12 13l8.5-6.5" stroke="var(--paper)" stroke-width="1.6"/></svg>
          info@brightloopvents.us
        </li>
        <li class="contacts__item">
          <svg class="contacts__icon" viewBox="0 0 24 24" aria-hidden="true"><circle cx="12" cy="12" r="10"/><path d="M2 12h20M12 2c3 3 3 17 0 20M12 2c-3 3-3 17 0 20M4 7h16M4 17h16" stroke="var(--paper)" stroke-width="1.2" fill="none"/></svg>
          brightloopvents.us
        </li>
      </ul>
    </div>
  </section>

  <section class="card card--back" aria-label="Business card back">
    <div class="brand"><span class="brand__dot"></span>BrightLoop</div>
  </section>
</main>
</body>
</html>
```